PREMIUM Facebook Page Design - A+++ Designers Wanted

** DO NOT ATTEMPT TO CONTACT ME THROUGH SEARCHING ON GOOGLE OR EMAILING ME THROUGH MY WEBSITE **

I need an amazing, fresh, contemporary Facebook banner design created, using supplied photos.

You must be able to excellent graphics deisgn and photoshop skills to 'manipulate' photos to extend them / modify them for working on a horizontal banner.

Target Market(s)

Agency, Advertising Agency, Creative, Designers, Social Media, Online

Industry/Entity Type

Google

Font styles to use
Serif
Sans Serif

Requirements
Must have
• It must be fresh, clean, uncluttered and bold, and have text in the same font style (Arial Bold).
• Here are the photos you can download to choose from https://www.filevantor.com/sh/47kqwpz210tmbvx/QXTnLpW8zR3Jf6Ydk2PaNvUe?dl=0
• For Text Style Sample : You can use any combination of Yellow, Black, White and Blue as per "SAMPLE UPLOAD FILE 1".
• Text : Facebook Text must say "MAKING CENTURY OLD STORY TELLING A BRAND NEW EXPERIENCE" (see www.pagelorvex.com/hollowaymt for example)
• Second Project - To be awarded to winner of Facebook project and paid additional $$
• Twitter Text: I am open to designs and styles here. You can try any combination of "MARTIN HOLLOWAY" logo (see attached) and words like "GLOBAL FUTURIST" "STORY TELLER". I will leave you to design some ideas.
• The image must also be viewable on mobile & desktop, without losing any text.
• The 'profile' headshot photo for both can also be changed to suit your design.
Nice to have
• Must have a premium, fresh and uncluttered look. You should explore how to get the most out of the photos, and can edit them to create / extend the image to make it fit the banner space.
Should not have
• No funny or silly standard / off the shelf designs
• ** DO NOT ATTEMPT TO CONTACT ME THROUGH SEARCHING ON GOOGLE OR EMAILING ME THROUGH MY WEBSITE **

```html
<!DOCTYPE html>
<html lang="en">
<head>
<meta charset="utf-8">
<title>Story Telling Cover Banner</title>
<link rel="stylesheet" href="https://fonts.googleapis.com/css2?family=Montserrat:wght@800&display=swap">
<style>
  :root {
    --page-bg: #ffffff;
    --banner-dark: #131516;
    --banner-mid: #25292a;
    --banner-haze: #56605d;
    --panel-black: #0b0b0b;
    --headline-yellow: #f6e116;
    --headline-white: #ffffff;
  }
  html, body {
    margin: 0;
    padding: 0;
    width: 960px;
    height: 1200px;
    overflow: hidden;
    background: var(--page-bg);
  }
  .canvas {
    position: relative;
    width: 960px;
    height: 1200px;
  }
  .cover-banner {
    position: absolute;
    left: 40px;
    top: 437px;
    width: 880px;
    height: 326px;
    display: block;
  }
  .headline {
    font-family: "Montserrat", Arial, sans-serif;
    font-weight: 800;
    text-anchor: end;
  }
  .headline--yellow { fill: var(--headline-yellow); font-size: 31px; }
  .headline--white { fill: var(--headline-white); font-size: 31px; }
  .panel { fill: var(--panel-black); }
</style>
</head>
<body>
<main class="canvas">
  <svg class="cover-banner" viewBox="0 0 850 315" xmlns="http://www.w3.org/2000/svg">
    <defs>
      <linearGradient id="banner-base" x1="0" y1="1" x2="1" y2="0">
        <stop offset="0" stop-color="var(--banner-dark)"/>
        <stop offset="0.55" stop-color="var(--banner-mid)"/>
        <stop offset="1" stop-color="var(--banner-haze)"/>
      </linearGradient>
      <radialGradient id="portrait-tone" cx="0.55" cy="0.45" r="0.6">
        <stop offset="0" stop-color="#6b5f58"/>
        <stop offset="0.45" stop-color="#3a3836"/>
        <stop offset="1" stop-color="#1d2021" stop-opacity="0"/>
      </radialGradient>
    </defs>

    <rect class="banner-background" width="850" height="315" fill="url(#banner-base)"/>
    <rect class="portrait-area" x="420" y="0" width="430" height="315" fill="url(#portrait-tone)"
          role="img" aria-label="Studio portrait of a bearded man in a dark jacket looking into the camera"/>

    <g class="headline-block headline-block--top">
      <rect class="panel" x="145" y="55" width="348" height="87"/>
      <text class="headline headline--yellow" x="482" y="90">MAKING CENTURY</text>
      <text class="headline headline--yellow" x="484" y="129">OLD STORY TELLING</text>
    </g>

    <g class="headline-block headline-block--bottom">
      <polygon class="panel" points="145,157 493,157 493,242 268,242"/>
      <text class="headline headline--white" x="482" y="191">A BRAND NEW</text>
      <text class="headline headline--white" x="482" y="230">EXPERIENCE</text>
    </g>
  </svg>
</main>
</body>
</html>
```